Zielgruppe
Wir sind eine Weiterbildungsfirma mit der Zielgruppe Unternehmer, Selbstständige, Führungskräfte und Vertriebler.
Aufgabenstellung
Es soll dynamisch, elegant und professionell wirken. Der Titel muss gut lesbar sein.
(Wir haben einen Pixmora-Foto-Account auf Abo-Basis.)
Der Titel lautet neu: Die Kelbing-Prinzipien für echte Durchbrüche

```html
<!DOCTYPE html>
<html lang="de">
<head>
<meta charset="utf-8">
<title>Die Kelbing-Prinzipien für echte Durchbrüche – Buchcover</title>
<link rel="stylesheet" href="https://fonts.googleapis.com/css2?family=Montserrat:wght@400;500;700&display=swap">
<style>
  :root {
    --page-bg: #ecebe8;
    --cover-white: #f7f7f5;
    --ink: #1f1f22;
    --brand-red: #c8203d;
    --slate: #43424b;
    --muted: #55545c;
  }
  html, body {
    margin: 0;
    padding: 0;
    width: 864px;
    height: 1200px;
    overflow: hidden;
    background: var(--page-bg);
  }
  .canvas {
    position: relative;
    width: 864px;
    height: 1200px;
  }
  .book-cover {
    position: absolute;
    left: 72px;
    top: 105px;
    width: 720px;
    height: 990px;
    background: var(--cover-white);
    box-shadow: 0 2px 10px rgba(0,0,0,0.08);
    overflow: hidden;
    font-family: "Montserrat", sans-serif;
  }
  .book-title {
    position: absolute;
    left: 16px;
    top: 60px;
    margin: 0;
    font-size: 45px;
    font-weight: 500;
    line-height: 1.22;
    color: var(--ink);
    letter-spacing: 0.2px;
  }
  .cover-artwork {
    position: absolute;
    left: 26px;
    top: 200px;
    width: 574px;
    height: 790px;
    background:
      linear-gradient(155deg, var(--brand-red) 0%, var(--brand-red) 32%, #e9e6e4 46%, var(--slate) 70%, var(--slate) 100%);
  }
  .author-name {
    position: absolute;
    left: 640px;
    top: 205px;
    writing-mode: vertical-rl;
    font-size: 20px;
    font-weight: 500;
    color: var(--muted);
    letter-spacing: 0.5px;
  }
  .publisher-mark {
    position: absolute;
    right: 18px;
    bottom: 28px;
    display: flex;
    align-items: center;
    gap: 8px;
    font-size: 13px;
    font-weight: 700;
    color: var(--brand-red);
    letter-spacing: 0.5px;
  }
  .publisher-mark .mark-square {
    width: 14px;
    height: 14px;
    background: var(--brand-red);
  }
</style>
</head>
<body>
  <main class="canvas">
    <article class="book-cover">
      <h1 class="book-title">Die Kelbing-Prinzipien für<br>echte Durchbrüche</h1>
      <div class="cover-artwork" role="img" aria-label="Abstrakte geometrische Illustration in Rot, Weiß und Schiefergrau: zwei stilisierte Figuren auf Stufen, eine steigt nach oben"></div>
      <span class="author-name">Jonas Kelbing</span>
      <div class="publisher-mark">
        <span class="mark-square"></span>
        <span class="mark-name">JONAS KELBING</span>
      </div>
    </article>
  </main>
</body>
</html>
```